Book Cover design - Education & Research

We need a design of the book cover for a book written in an education sector. It has been written by a professor with target audience being other professors, lecturers, PhD students etc. The book is about Singapore's development as a country (from third world to economical leader) with high emphasis on it's education sector. It explores many education concepts that could set an example for other countries.
We would like the design to be serious, modern, representing innovation, progress in the educations space. The colours will be mainly red and white representing the country's flag. Probably white background with red additions. The design will consist of three parts:
1) Front cover (the most important where the designer should put most effort in). At the top will be name of the author: Zofia Kradecka, below name of the book: "Odlegle Sciezki Nauczania" with smaller subtitle below: "Zielone Mosty Pomiedzy Szkolami Zielone Mosty Pomiedzy Szkolami"
2) Back cover (very simple with majority of the space put for text, reviews etc.)
3) Second page already inside the book (less important, just a simple black and white design in this part)
We welcome any creative designs from your part, but for reference below is an idea of how we would like it to look like. I would recommend for the designers to do two designs. One according to the below instructions and another with your own idea how to go about it. Please do keep in mind that we can't use proprietary Singapore icons like quorvex or exact design of Singapore flag, so please don't use these.
Our idea:
- The front page to have cityscape with silhouettes of Singapore iconic buildings (Coral Hill Towers, Halvern Wheel, Lumen Craft Gallery, Corvanta, Terraces of Wrenfield, Sky scrappers)
- A red and white ribbon starting at the front and then going through the spine of the book to the back cover.
NOTE:
- We would like to see more designs with your own creativity and other colors, not only red and white
Education sector, Universities, Professors

```html
<!DOCTYPE html>
<html lang="pl">
<head>
<meta charset="utf-8">
<title>Odlegle Sciezki Nauczania – okładka</title>
<link rel="stylesheet" href="https://fonts.googleapis.com/css2?family=Barlow+Condensed:wght@500;600&family=Cormorant+Garamond:wght@500;700&family=Tinos&display=swap">
<style>
  :root {
    --backdrop: #dcc4c7;
    --sky-light: #f4f5f6;
    --sky-mid: #d9dcdf;
    --sky-deep: #b9bdc2;
    --flag-red: #e32a2f;
    --flag-white: #ffffff;
    --city-red: #8c1519;
    --city-dark: #5e0d10;
    --ink: #141414;
    --title-red: #d4242c;
  }
  * { margin: 0; padding: 0; box-sizing: border-box; }
  html, body { width: 1200px; height: 1200px; overflow: hidden; }
  body { background: var(--backdrop); position: relative; }

  .cover-wrap {
    position: absolute; left: 40px; top: 202px;
    width: 1120px; height: 795px; overflow: hidden;
    box-shadow: 0 8px 24px rgba(0,0,0,.18);
  }
  .sky {
    position: absolute; inset: 0;
    background:
      radial-gradient(ellipse 40% 18% at 25% 30%, rgba(255,255,255,.9), transparent 70%),
      radial-gradient(ellipse 35% 16% at 75% 48%, rgba(255,255,255,.85), transparent 70%),
      radial-gradient(ellipse 45% 20% at 55% 15%, rgba(255,255,255,.8), transparent 70%),
      linear-gradient(180deg, var(--sky-mid) 0%, var(--sky-light) 35%, var(--sky-deep) 60%, var(--sky-light) 75%);
  }
  .ribbon { position: absolute; inset: 0; }
  .skyline {
    position: absolute; left: 0; right: 0; top: 400px; bottom: 0;
    background: linear-gradient(180deg,
      rgba(140,21,25,0) 0%,
      rgba(140,21,25,.35) 35%,
      rgba(120,17,21,.55) 60%,
      var(--city-red) 68%,
      var(--city-dark) 100%);
  }
  .spine {
    position: absolute; left: 513px; top: 0; width: 94px; height: 100%;
    background: rgba(255,255,255,.28);
    border-left: 1px solid rgba(255,255,255,.5);
    border-right: 1px solid rgba(255,255,255,.5);
  }
  .spine-title {
    position: absolute; left: 50%; top: 100px;
    transform-origin: 0 0;
    transform: rotate(90deg) translate(0, -50%);
    white-space: nowrap;
    font-family: "Tinos", "Times New Roman", serif;
    font-size: 27px; letter-spacing: 7px; color: var(--ink);
  }
  .back {
    position: absolute; left: 40px; top: 90px; width: 460px;
    font-family: "Tinos", "Times New Roman", serif; color: var(--ink);
  }
  .back-heading { font-weight: 700; font-size: 17px; margin-bottom: 18px; }
  .back-body { font-size: 16.5px; line-height: 23.3px; text-align: justify; }
  .front {
    position: absolute; left: 607px; top: 0; width: 513px;
    text-align: center; color: var(--ink);
  }
  .author {
    margin-top: 48px;
    font-family: "Barlow Condensed", "Arial Narrow", sans-serif;
    font-weight: 600; font-size: 27px; letter-spacing: 7px;
  }
  .title { margin-top: 24px; font-family: "Cormorant Garamond", "Times New Roman", serif; line-height: 1; }
  .title-lead { display: block; color: var(--title-red); font-weight: 700; font-size: 58px; letter-spacing: 1px; }
  .title-rest { display: block; margin-top: 10px; font-weight: 500; font-size: 54px; letter-spacing: 2px; }
  .subtitle {
    margin-top: 18px;
    font-family: "Barlow Condensed", "Arial Narrow", sans-serif;
    font-weight: 500; font-size: 22px; letter-spacing: 3px;
  }
</style>
</head>
<body>
  <main class="cover-wrap">
    <div class="sky" role="img" aria-label="Cloudy grey and white sky photograph"></div>

    <svg class="ribbon" width="1120" height="795" viewBox="0 0 1120 795" aria-hidden="true">
      <path d="M0 565 L560 540 L1120 488 L1120 700 L0 700 Z" fill="var(--flag-white)"/>
      <path d="M0 565 L560 540 L1120 488 L1120 532 L560 570 L0 588 Z" fill="var(--flag-red)"/>
    </svg>

    <div class="skyline" role="img" aria-label="Dark red textured city skyline silhouette with skyscrapers, Coral Hill Towers, the Halvern Wheel, Lumen Craft Gallery and Terraces of Wrenfield"></div>

    <section class="back">
      <h2 class="back-heading">Book Details :</h2>
      <p class="back-body">Sample text....Sample text....Sample text....Sample text....Sample text....Sample text....Sample text....Sample text....Sample text....Sample text....Sample text....Sample text....Sample text....Sample text....Sample text....Sample text....Sample text....Sample text....Sample text....Sample text....Sample text....Sample text....Sample text....Sample text....Sample text....Sample text....Sample text....Sample text....Sample text....Sample text....Sample text....Sample text....Sample text....Sample text....Sample text....</p>
    </section>

    <div class="spine">
      <span class="spine-title">ODLEGLE SCIEZKI NAUCZANIA</span>
    </div>

    <section class="front">
      <p class="author">ZOFIA KRADECKA</p>
      <h1 class="title">
        <span class="title-lead">ODLEGLE</span>
        <span class="title-rest">SCIEZKI NAUCZANIA</span>
      </h1>
      <p class="subtitle">Zielone Mosty Pomiedzy Szkolami</p>
    </section>
  </main>
</body>
</html>
```